Bottle design for a range of water enhancers

We need a bottle designed for a new range of water enhancers manufactured by the company, Vemo Kettle based in Lahore, Pakistan. The product is called "Vemo" and comes in 6 different flavors/colors. In essence, Vemo is a zero sugar, zero calorie flavor concentrate that is squirted in a glass of water directly from the bottle to make a refreshing beverage. The bottle size is about 60 ml. The bottle needs to be stylish, unique and must have a premium/high-end look to it. The shape of the bottle must be relatively flat. The bottle must be able to translate in to different colors according to the flavor.Some potential sketches have been added for reference.

Target Market(s)

Target market has been identified between the ages of 18 to 35

Colors

Designer to choose colors to be used in the design.

Requirements
Must have
• a sleek, eye catching design.
Nice to have
• A transparent section of the bottle where you can see the liquid inside.
Should not have
• bulky shapes

```html
<!DOCTYPE html>
<html lang="en">
<head>
<meta charset="utf-8">
<title>Vemo – Liquid Water Enhancer Bottle</title>
<link href="https://fonts.googleapis.com/css2?family=Lato:wght@400;700&display=swap" rel="stylesheet">
<style>
  :root {
    --bg: #000000;
    --cap-top: #ffb515;
    --cap-bottom: #f0851c;
    --body-dark: #050505;
    --white: #ffffff;
    --accent-orange: #f7a21b;
    --natural-green: #5cb82e;
    --poly-green: #3f9a2a;
    --poly-yellow: #f7d23a;
    --poly-orange: #f49a25;
    --poly-teal: #6fb9b4;
    --poly-purple: #9a3fd6;
    --poly-magenta: #e0279e;
  }
  html, body {
    margin: 0;
    padding: 0;
    width: 1200px;
    height: 1200px;
    overflow: hidden;
    background: var(--bg);
  }
  .canvas {
    position: relative;
    width: 1200px;
    height: 1200px;
    background: var(--bg);
  }
  .bottles {
    position: absolute;
    left: 0;
    top: 0;
    width: 1200px;
    height: 1200px;
  }
  .label-text {
    font-family: "Lato", sans-serif;
    fill: var(--white);
  }
  .brand-name { font-size: 96px; font-weight: 400; letter-spacing: 1px; }
  .tagline { font-size: 18px; fill: var(--accent-orange); letter-spacing: 1px; }
  .claim { font-size: 18px; letter-spacing: 0.5px; }
  .servings-small { font-size: 18px; letter-spacing: 0.5px; }
  .servings-number { font-size: 52px; font-weight: 400; }
</style>
</head>
<body>
<div class="canvas">
  <svg class="bottles" viewBox="0 0 1200 1200" width="1200" height="1200" xmlns="http://www.w3.org/2000/svg">
    <defs>
      <linearGradient id="capFill" x1="0" y1="0" x2="0" y2="1">
        <stop offset="0" stop-color="var(--cap-top)"/>
        <stop offset="1" stop-color="var(--cap-bottom)"/>
      </linearGradient>
      <linearGradient id="baseTones" x1="0" y1="0" x2="1" y2="1">
        <stop offset="0" stop-color="var(--poly-orange)"/>
        <stop offset="0.35" stop-color="var(--poly-yellow)"/>
        <stop offset="0.6" stop-color="var(--poly-orange)"/>
        <stop offset="1" stop-color="var(--poly-magenta)"/>
      </linearGradient>
      <radialGradient id="greenGlow" cx="0.5" cy="0.5" r="0.5">
        <stop offset="0" stop-color="var(--poly-green)" stop-opacity="0.95"/>
        <stop offset="1" stop-color="var(--poly-green)" stop-opacity="0"/>
      </radialGradient>
      <radialGradient id="tealGlow" cx="0.5" cy="0.5" r="0.5">
        <stop offset="0" stop-color="var(--poly-teal)" stop-opacity="0.95"/>
        <stop offset="1" stop-color="var(--poly-teal)" stop-opacity="0"/>
      </radialGradient>
      <radialGradient id="purpleGlow" cx="0.5" cy="0.5" r="0.5">
        <stop offset="0" stop-color="var(--poly-purple)" stop-opacity="1"/>
        <stop offset="1" stop-color="var(--poly-purple)" stop-opacity="0"/>
      </radialGradient>
      <radialGradient id="yellowGlow" cx="0.5" cy="0.5" r="0.5">
        <stop offset="0" stop-color="var(--poly-yellow)" stop-opacity="1"/>
        <stop offset="1" stop-color="var(--poly-yellow)" stop-opacity="0"/>
      </radialGradient>
      <linearGradient id="topFade" x1="0" y1="0" x2="0" y2="1">
        <stop offset="0" stop-color="#fff" stop-opacity="0"/>
        <stop offset="0.4" stop-color="#fff" stop-opacity="1"/>
        <stop offset="1" stop-color="#fff" stop-opacity="1"/>
      </linearGradient>
      <mask id="frontFade">
        <rect x="230" y="580" width="500" height="345" fill="url(#topFade)"/>
      </mask>
      <mask id="sideFade">
        <rect x="755" y="600" width="190" height="320" fill="url(#topFade)"/>
      </mask>
      <linearGradient id="sideTones" x1="0" y1="0" x2="0.6" y2="1">
        <stop offset="0" stop-color="var(--poly-orange)"/>
        <stop offset="0.45" stop-color="var(--poly-orange)"/>
        <stop offset="0.7" stop-color="var(--poly-purple)"/>
        <stop offset="1" stop-color="var(--poly-magenta)"/>
      </linearGradient>
      <linearGradient id="edgeShade" x1="0" y1="0" x2="1" y2="0">
        <stop offset="0" stop-color="#2a2a2a"/>
        <stop offset="0.12" stop-color="#050505"/>
        <stop offset="0.88" stop-color="#050505"/>
        <stop offset="1" stop-color="#2a2a2a"/>
      </linearGradient>
      <clipPath id="frontBody">
        <path d="M243 360 L713 360 C690 460 688 740 711 860 Q714 918 658 918 L300 918 Q244 918 247 860 C270 740 268 460 243 360 Z"/>
      </clipPath>
      <clipPath id="sideBody">
        <path d="M764 371 L936 371 C922 470 920 760 934 860 Q938 908 905 908 L795 908 Q762 908 766 860 C780 760 778 470 764 371 Z"/>
      </clipPath>
    </defs>

    <g class="bottle-front">
      <path class="bottle-cap" d="M243 360 L713 360 C700 330 685 300 665 280 Q658 272 645 272 L310 272 Q297 272 290 280 C270 300 255 330 243 360 Z" fill="url(#capFill)"/>
      <g class="bottle-body" clip-path="url(#frontBody)">
        <rect x="230" y="355" width="500" height="570" fill="url(#edgeShade)"/>
        <g role="img" aria-label="Colourful low-poly facet pattern with halftone dots" mask="url(#frontFade)">
          <rect x="230" y="580" width="500" height="345" fill="url(#baseTones)"/>
          <ellipse cx="320" cy="650" rx="120" ry="80" fill="url(#greenGlow)"/>
          <ellipse cx="360" cy="760" rx="110" ry="80" fill="url(#yellowGlow)"/>
          <ellipse cx="480" cy="720" rx="110" ry="80" fill="url(#tealGlow)"/>
          <ellipse cx="600" cy="840" rx="150" ry="110" fill="url(#purpleGlow)"/>
        </g>
      </g>

      <text class="label-text brand-name" x="472" y="548" text-anchor="middle">Vemo</text>
      <text class="label-text tagline" x="478" y="578" text-anchor="middle">LIQUID WATER ENHANCER</text>

      <text class="label-text claim" x="427" y="614" text-anchor="middle">100%</text>
      <rect class="natural-badge" x="458" y="598" width="96" height="21" fill="var(--natural-green)"/>
      <text class="label-text claim" x="506" y="614" text-anchor="middle">NATURAL</text>
      <text class="label-text claim" x="478" y="638" text-anchor="middle">INGREDIENTS</text>

      <line x1="376" y1="846" x2="446" y2="846" stroke="var(--white)" stroke-width="1.5"/>
      <line x1="510" y1="846" x2="605" y2="846" stroke="var(--white)" stroke-width="1.5"/>
      <text class="label-text servings-small" x="412" y="865" text-anchor="middle">MAKES</text>
      <text class="label-text servings-number" x="478" y="869" text-anchor="middle">30</text>
      <text class="label-text servings-small" x="557" y="865" text-anchor="middle">SERVINGS</text>
    </g>

    <g class="bottle-side">
      <path class="bottle-cap" d="M764 371 L936 371 C925 335 910 305 892 289 Q889 286 884 286 L814 286 Q809 286 806 289 C788 305 774 335 764 371 Z" fill="url(#capFill)"/>
      <g class="bottle-body" clip-path="url(#sideBody)">
        <rect x="755" y="365" width="190" height="550" fill="url(#edgeShade)"/>
        <rect role="img" aria-label="Side view of the colourful facet pattern" x="755" y="600" width="190" height="320" fill="url(#sideTones)" mask="url(#sideFade)"/>
      </g>
    </g>
  </svg>
</div>
</body>
</html>
```